Stationary design for boutique production house

We need a stationary design for our production house, 'Luma Studios' based in Singapore. We produce microfilms as well as podcasts, talkshows and events. Our logo is a stylized icon of our director, who is also the executive producer and host of our programs, Orla. Our main company colors are Red, Black and white. We would like a clean, minimalist design incorporating our existing company logo that conveys a sense of urbanism and elegance.

Logo and font files are attached. f

Target Market(s)

We focus on lifestyle media rather than entertainment.

Industry/Entity Type

Boutique

Font styles to use
Serif
Sans Serif

Colors
ec1f27
ffffff
000000

Requirements
Must have
• Our company logo and at least one of our company colors.
Nice to have
• Our address and contact information.
Should not have
• Changes made to the company logo (using only certain parts of it is fine though)

```html
<!DOCTYPE html>
<html lang="en">
<head>
<meta charset="utf-8">
<title>Luma Studios – Business Card</title>
<link rel="stylesheet" href="https://fonts.googleapis.com/css2?family=PT+Serif:wght@400;700&display=swap">
<style>
  :root {
    --brand-red: #ec1f27;
    --ink: #000000;
    --paper: #ffffff;
    --backdrop: #e9e6e2;
    --panel-dark-top: #2a2a2c;
    --panel-dark-bottom: #0d0d0e;
    --panel-text: #d9d9d9;
    --frost-light: #f4f4f3;
    --frost-mid: #dcdcdb;
  }
  * { box-sizing: border-box; margin: 0; padding: 0; }
  html, body {
    width: 1200px; height: 969px; overflow: hidden;
    background: var(--backdrop);
    font-family: "PT Serif", Georgia, serif;
  }
  .canvas { position: relative; width: 1200px; height: 969px; }
  .card {
    position: absolute; left: 100px; top: 200px;
    width: 1000px; height: 570px;
    border-radius: 26px; overflow: hidden;
    display: flex;
    box-shadow: 0 18px 40px rgba(0,0,0,.18);
  }
  .card-info {
    position: relative; width: 480px; height: 100%;
    background: linear-gradient(160deg, var(--panel-dark-top), var(--panel-dark-bottom));
    color: var(--panel-text);
    padding: 70px 0 0 66px;
  }
  .card-divider { width: 4px; background: var(--brand-red); }
  .card-brand {
    flex: 1; position: relative;
    background: linear-gradient(150deg, var(--frost-light), var(--frost-mid));
    display: flex; align-items: center; justify-content: center;
  }
  .person-name {
    color: var(--brand-red); font-size: 32px; font-weight: 700;
    letter-spacing: 1px; line-height: 1.2;
  }
  .person-role { font-size: 25px; margin-top: 6px; }
  .address { font-size: 23px; line-height: 36px; margin-top: 60px; font-style: normal; }
  .contacts { list-style: none; margin-top: 30px; }
  .contacts li {
    display: flex; align-items: center; height: 40px; font-size: 23px;
  }
  .contacts svg { width: 22px; height: 22px; margin-right: 21px; fill: var(--brand-red); flex-shrink: 0; }
  .brand-name {
    font-size: 40px; font-weight: 700; color: var(--ink);
    letter-spacing: 1px; text-transform: uppercase; white-space: nowrap;
  }
</style>
</head>
<body>
<main class="canvas">
  <article class="card">
    <section class="card-info">
      <h1 class="person-name">DANIEL REYES</h1>
      <p class="person-role">CEO/Founder</p>
      <address class="address">
        214 Kestrel Row<br>
        Tanjong Bay, Singapore 408712
      </address>
      <ul class="contacts">
        <li>
          <svg viewBox="0 0 24 24" aria-hidden="true"><path d="M6.6 10.8a15 15 0 0 0 6.6 6.6l2.2-2.2c.3-.3.7-.4 1-.2 1.1.4 2.3.6 3.6.6.6 0 1 .4 1 1V20c0 .6-.4 1-1 1A17 17 0 0 1 3 4c0-.6.4-1 1-1h3.5c.6 0 1 .4 1 1 0 1.3.2 2.5.6 3.6.1.3 0 .7-.2 1z"/></svg>
          612 480 1173
        </li>
        <li>
          <svg viewBox="0 0 24 24" aria-hidden="true"><path d="M7 1h10a2 2 0 0 1 2 2v18a2 2 0 0 1-2 2H7a2 2 0 0 1-2-2V3a2 2 0 0 1 2-2zm0 3v14h10V4zm5 15.2a1.2 1.2 0 1 0 0 2.4 1.2 1.2 0 0 0 0-2.4z"/></svg>
          845 207 3391
        </li>
        <li>
          <svg viewBox="0 0 24 24" aria-hidden="true"><path d="M6 2h12v5H6zM3 8h18a2 2 0 0 1 2 2v7h-4v5H5v-5H1v-7a2 2 0 0 1 2-2zm4 8v4h10v-4z"/></svg>
          431 765 2208
        </li>
        <li>
          <svg viewBox="0 0 24 24" aria-hidden="true"><path d="M2 5h20v14H2zm2 2v.5l8 5 8-5V7zm0 2.9V17h16V9.9l-8 5z"/></svg>
          hello@lumastudios.sg
        </li>
        <li>
          <svg viewBox="0 0 24 24" aria-hidden="true"><path d="M12 2a10 10 0 1 0 0 20 10 10 0 0 0 0-20zm-1 17.9A8 8 0 0 1 4.2 10L9 14.8V16a2 2 0 0 0 2 2zm6.9-2.5A2 2 0 0 0 16 16h-1v-3a1 1 0 0 0-1-1H8v-2h2a1 1 0 0 0 1-1V7h2a2 2 0 0 0 2-2v-.4a8 8 0 0 1 2.9 12.8z"/></svg>
          www.lumastudios.sg
        </li>
      </ul>
    </section>
    <div class="card-divider"></div>
    <section class="card-brand">
      <p class="brand-name">Luma Studios</p>
    </section>
  </article>
</main>
</body>
</html>
```